Dr Lenora aesthetics - Grace Distilled

I need a logo design for a new aesthetics business in London. I am specialised in Botox, Dermal Fillers & Skin Pigmentation treatment. The slogan is Grace Distilled. I would like some of the writing on the card to be embossed. I would like a very elegant design with the following detail:

1. White and gray scale background. For the font colour try gold OR silver shades.
2. The business involves working on the face mostly. Anything that can be done with letter 'M'? Or any other logo?
3. The front of the card should have Dr Lenora Aesthetics and the slogan 'Grace Distilled'. The back should have my full name (Dr Lenora Brackwell), qualifications (MBBS MSC BSC), my website (www.ashfernclinicalcare.example), telephone number & email.
4. The back should also say treatments offered: ANTI-WRINKLE INJECTIONS. DERMAL FILLERS, LIP ENHANCEMENT, HYPERHYDROSIS. SKIN PIGMENTATION

Thank you very much
Updates

Project Deadline Extended
Reason: Delays in market research response. I would be grateful for an extension please. Many thanks

Target Market(s)

Female and male aged 18 and above

Industry/Entity Type

Business

Contact Information for Business Card

Elegant design. Square corners. British standard size. Horizontal design. Should contain the slogan, contact details.

Font styles to use
Script

Colors
c9c9c9
fbed22
ffffff
f5f5f5
000000

Requirements
Must have
• All that's mentioned above
Nice to have
• A logo with the outline of a female face. Or anything that can be done with the letter M of Lenora.
Should not have
• No colours like green / purple / orange

```html
<!DOCTYPE html>
<html lang="en">
<head>
<meta charset="utf-8">
<title>Dr Lenora Aesthetics – Business Card</title>
<link rel="stylesheet" href="https://fonts.googleapis.com/css2?family=Pinyon+Script&family=PT+Sans:wght@700&family=Questrial&display=swap">
<style>
  :root {
    --stage: #7a7a7a;
    --stage-edge: #5e5e5e;
    --card-black: #000000;
    --card-grey: #c9c9c9;
    --gold: #fbed22;
    --white: #ffffff;
    --ink: #111111;
  }
  * { margin: 0; padding: 0; box-sizing: border-box; }
  html, body { width: 990px; height: 1200px; overflow: hidden; }
  body {
    position: relative;
    background: radial-gradient(ellipse at center, var(--stage) 55%, var(--stage-edge) 100%);
    font-family: "Questrial", "Century Gothic", sans-serif;
  }
  .side-label {
    position: absolute;
    color: var(--white);
    font-family: "PT Sans", Arial, sans-serif;
    font-weight: 700;
    font-size: 30px;
    line-height: 1;
  }
  .side-label--front { left: 128px; top: 26px; }
  .side-label--back { left: 831px; top: 1163px; }

  .card {
    position: absolute;
    left: 54px;
    width: 881px;
    height: 514px;
    box-shadow: 0 6px 22px rgba(0,0,0,.55);
  }
  .card--front { top: 71px; background: var(--card-black); }
  .card--back { top: 622px; background: var(--card-grey); }

  .brand-title {
    position: absolute;
    left: 171px;
    top: 84px;
    font-family: "PT Sans", Arial, sans-serif;
    font-weight: 700;
    font-size: 41px;
    color: var(--gold);
    text-shadow: 0 0 8px rgba(251,237,34,.55);
    white-space: nowrap;
  }
  .brand-slogan {
    position: absolute;
    left: 196px;
    top: 120px;
    font-family: "Pinyon Script", cursive;
    font-size: 34px;
    color: var(--white);
    white-space: nowrap;
  }
  .brand-mark {
    position: absolute;
    display: flex;
    align-items: center;
    justify-content: center;
    color: var(--gold);
    font-family: "Questrial", "Century Gothic", sans-serif;
    white-space: nowrap;
  }
  .brand-mark--small { left: 86px; top: 280px; width: 156px; height: 139px; font-size: 40px; }
  .brand-mark--large { left: 402px; top: 51px; width: 436px; height: 360px; font-size: 112px; }

  .website {
    position: absolute;
    right: 95px;
    top: 402px;
    font-size: 22px;
    color: var(--white);
    white-space: nowrap;
  }

  .treatments {
    position: absolute;
    left: 60px;
    width: 293px;
    top: 104px;
    text-align: right;
    color: var(--ink);
  }
  .treatments__heading { font-size: 27px; font-weight: 400; line-height: 32px; }
  .treatments__list { list-style: none; font-size: 20px; line-height: 26px; }

  .practitioner {
    position: absolute;
    left: 394px;
    top: 416px;
    font-family: "PT Sans", Arial, sans-serif;
    font-weight: 700;
    font-size: 19px;
    color: var(--ink);
    white-space: nowrap;
  }
  .rule {
    position: absolute;
    left: 51px;
    top: 455px;
    width: 776px;
    height: 4px;
    background: var(--white);
  }
</style>
</head>
<body>
  <div class="side-label side-label--front">front</div>

  <section class="card card--front" aria-label="Card front">
    <h1 class="brand-title">Dr Lenora Aesthetics</h1>
    <p class="brand-slogan">Grace Distilled</p>
    <div class="brand-mark brand-mark--small">Lenora</div>
    <p class="website">www.ashfernclinicalcare.example</p>
  </section>

  <section class="card card--back" aria-label="Card back">
    <div class="treatments">
      <h2 class="treatments__heading">Treatments Offered:</h2>
      <ul class="treatments__list">
        <li>Anti-Wrinkle Injections.</li>
        <li>Dermal Fillers,</li>
        <li>Lip Enhancement,</li>
        <li>Hyperhydrosis.</li>
        <li>Skin Pigmentation</li>
      </ul>
    </div>
    <div class="brand-mark brand-mark--large">Lenora</div>
    <p class="practitioner">Dr. Lenora Brackwell, MBBS. MSC. BSC</p>
    <div class="rule"></div>
  </section>

  <div class="side-label side-label--back">back</div>
</body>
</html>
```